Artist needs a Wordpress Website design to market my original paintings

Mona Breckell Gallery.com
Artist - Original Abstract Paintings

Artist needs classy and elegant WORDPRESS website to market my Original Paintings.
What sets these paintings apart?
Each one was inspired by the inner connection between the artist and the individual destined to receive the painting. Paintings are priced high end and require a website to reflect their high quality.
Website must be responsive on all devices. eg. mobile, laptop and desktop. It must have a shopping cart in order to complete sales.
The domain name monabreckellgallery.com has already been purchased and is hosted on Servanta.
I want it to be very easy to navigate and also easy for me to add and edit more images and content.
I have no official logo but you can insert the title,
Mona Breckell
Collection
Original Fluid Art Paintings
in whatever design/font format you feel attractive, I leave that to the designer. I want it to be simple and include a lot of negative space to avoid a cluttered look. The paintings are colorful on their own and prefer not to detract from them as a focal point. I leave the color theme to the designer. Perhaps you may like to extract a color theme from one of the paintings.
Requirements:
5 pages: HOME, ABOUT, SHOP, CART, CONTACT
Home page:
-Menu across the top
-1 large painting (prefer the purple and green painting)
-3 smaller images below the large one
Unless you come up with a more professional format.
ABOUT:
(You can include my uploaded photo for now on the ABOUT page. I will replace it when I get a professional photo.)
I learned I am never too old to re-invent my life. Lesson learned. At the age of 78 and after the ending of my 30 years of marriage I was faced with an unexpected change in my life circumstances. I made the decision to re-invent my life.
Art, in varying media has always been a part of my experience as a hobby. When I was presented with fluid art, my life as I had known it turned to excitement, and discovery, carving a promising vision of my future.
My spiritual training has taught me how to recognize my connection with people inwardly. With this awareness it became clear to me while painting that I was creating a work of art for a specific individual. I allow creative expression to flow through me that is destined for you. I do not know who you are, but if you recognize the painting that inspires you, I have succeeded with our connection.
I live in Washington State, USA
I am looking forward to meeting you.
Mona Breckell
SHOP:
This should be the gallery from which one can shop. The images will be more like a thumbprint but large enough to see well, perhaps 3 across the page. As one hovers over, or clicks on one, it will link to a page with a larger view that has:
-Description
-Price and a CHOICE to click on
-Add to Cart Button OR
-Continue shopping (so they don't have to go back to homepage)
This page should be a scrolling one so eventually all of my paintings will be added to this page and easy for someone to shop instead of going back and forth between pages.
Please set this up (making it a link to larger image, etc) and include one or all of the images I upload here. I will add the rest.

CART:
-Add a shopping cart

CONTACT:
-email: breckellgallery@mailorbit.net
All pages should have a link back to the homepage.
SOCIAL MEDIA LINKS:
-Snapvista:
http://snapvista.net/monabreckellgallery
-Friendloop
https://www.friendloop.net/ourchosenworks/?
view_public_for=407385291164273

http://corinnalubeckstudio.net
eg of a website that I like the navigation. I like the simplicity of the Home Page but the photo is too large. A smaller main photo and 3 smaller ones beneath it would have looked nicer to me.

```html
<!DOCTYPE html>
<html lang="en">
<head>
<meta charset="utf-8">
<title>Mona Breckell – Original Fluid Art Paintings</title>
<link rel="stylesheet" href="https://fonts.googleapis.com/css2?family=Merriweather:wght@400;700&family=Montserrat:wght@500;600&family=Poppins:wght@400;500&display=swap">
<style>
:root{
  --plum:#6b5a78;
  --plum-text:#6b4f8a;
  --lilac:#9c86b5;
  --nav-active:#7a6688;
  --ink:#222;
  --mint:#a8e0d2;
  --teal-dark:#2e5c5c;
  --footer:#2b5a60;
  --footer-base:#1e3c48;
  --footer-text:#e3ecec;
  --muted:#666;
  --rule:#e6e6e6;
  --paper:#e9ecec;
  --white:#fff;
}
*{margin:0;padding:0;box-sizing:border-box}
html,body{width:837px;height:1200px;overflow:hidden;background:var(--white)}
.page{position:relative;width:837px;height:1200px;overflow:hidden;font-family:'Poppins',sans-serif}
.abs{position:absolute}

.brand-band{left:308px;top:22px;width:223px;height:48px;background:var(--plum);border-radius:3px;display:flex;align-items:center;justify-content:center}
.brand-name{font-family:'Merriweather',serif;font-weight:400;color:var(--white);font-size:21px;letter-spacing:.5px}
.tagline{left:0;width:837px;top:80px;text-align:center;font-family:'Montserrat',sans-serif;font-weight:500;font-size:9px;color:var(--plum-text);letter-spacing:.4px}

.nav{top:122px;left:0;width:837px;height:16px;font-family:'Merriweather',serif;font-size:10px;color:var(--ink)}
.nav span{position:absolute;top:0}
.nav .active{color:var(--nav-active)}
.nav svg{position:absolute;top:1px}
.cart-count{position:absolute;left:532px;top:-2px;width:7px;height:7px;border-radius:50%;background:var(--plum);color:var(--white);font-size:5px;line-height:7px;text-align:center;font-family:'Poppins',sans-serif}

.hero{left:0;top:160px;width:837px;height:360px;background:linear-gradient(115deg,#2f5a3a 0%,#4fd49a 30%,#3ee6a8 50%,#b58fc4 70%,#4a3a63 90%,#2b2540 100%)}
.fade-top{left:0;top:156px;width:837px;height:26px;background:linear-gradient(180deg,var(--white) 0%,var(--white) 25%,rgba(233,236,236,.85) 50%,rgba(255,255,255,0) 100%)}
.fade-bottom{left:0;top:494px;width:837px;height:30px;background:linear-gradient(0deg,var(--white) 0%,var(--white) 25%,rgba(233,236,236,.85) 50%,rgba(255,255,255,0) 100%)}
.hero-dots{left:798px;top:284px}
.hero-dots i{display:block;width:5px;height:5px;border-radius:50%;border:1px solid #111;margin-bottom:4px}
.hero-dots i.on{background:#111}

.section-badge{left:343px;top:552px;width:162px;height:36px;background:var(--mint);border-radius:2px;display:flex;align-items:center;justify-content:center;font-family:'Merriweather',serif;font-weight:700;font-size:14px;color:var(--teal-dark)}
.intro{left:0;top:603px;width:837px;text-align:center;font-size:6.5px;line-height:10.5px;color:var(--muted);white-space:nowrap}

.card{top:664px;width:175px;height:199px;border:1px dashed #cfcfcf;border-top:none}
.card .art{height:165px}
.card .caption{position:absolute;left:12px;top:175px;font-family:'Montserrat',sans-serif;font-weight:600;font-size:7.5px;color:#333}
.card .zoom{position:absolute;right:7px;top:172px;width:19px;height:19px;border:1px dashed #999;border-radius:50%;display:flex;align-items:center;justify-content:center}
.art-warm{background:linear-gradient(135deg,#c9852a,#e6d2b0 45%,#c24f1e 75%,#d8cfc2)}
.art-night{background:linear-gradient(180deg,#0e1a3a 0%,#2b4d7a 40%,#7a96b0 70%,#b79e7a 100%)}

.shop-btn{left:357px;top:889px;width:121px;height:26px;background:var(--plum);color:var(--white);font-family:'Montserrat',sans-serif;font-weight:600;font-size:8.5px;letter-spacing:2.6px;display:flex;align-items:center;justify-content:center}

.rule{left:146px;width:544px;height:1px;background:var(--rule)}
.follow{left:322px;top:966px;font-family:'Merriweather',serif;font-size:11px;color:#444}
.social{top:964px;width:18px;height:18px;border-radius:50%;background:var(--lilac);color:var(--white);font-family:'Poppins',sans-serif;font-weight:500;font-size:8px;line-height:18px;text-align:center}

.footer{left:0;top:1017px;width:837px;height:146px;background:var(--footer)}
.footer-fade{left:0;top:1004px;width:837px;height:30px;background:linear-gradient(180deg,var(--white) 0%,var(--white) 30%,var(--paper) 55%,rgba(43,90,96,0) 100%)}
.col-title{top:1062px;font-family:'Merriweather',serif;font-size:7.5px;font-weight:400;color:var(--footer-text)}
.link{font-size:6.5px;color:var(--footer-text)}
.pay{top:1081px;width:20px;height:13px;border-radius:1.5px;background:#e9eef0;color:var(--footer);font-family:'Poppins',sans-serif;font-weight:500;font-size:4.6px;line-height:13px;text-align:center}
.base{left:0;top:1163px;width:837px;height:37px;background:var(--footer-base);color:var(--footer-text);font-family:'Montserrat',sans-serif;font-weight:500;font-size:7px;letter-spacing:.6px;display:flex;align-items:center;justify-content:center}
</style>
</head>
<body>
<div class="page">

  <header>
    <div class="abs brand-band"><span class="brand-name">Mona Breckell</span></div>
    <p class="abs tagline">Collection ~ Original Fluid Art Paintings</p>
    <nav class="abs nav">
      <span class="active" style="left:263px">HOME</span>
      <span style="left:309px">ABOUT</span>
      <span style="left:359px">SHOP</span>
      <span style="left:402px">CART</span>
      <span style="left:444px">CONTACT</span>
      <span style="left:507px">|</span>
      <svg style="left:526px" width="10" height="9" viewBox="0 0 10 9"><path d="M1 3h8l-1 5H2z" fill="#999"/><path d="M3 3l2-2 2 2" stroke="#999" fill="none"/></svg>
      <span class="cart-count">0</span>
      <svg style="left:547px" width="8" height="9" viewBox="0 0 8 9"><circle cx="4" cy="2.5" r="2.2" fill="#999"/><path d="M0 9c0-3 2-4 4-4s4 1 4 4z" fill="#999"/></svg>
      <svg style="left:566px" width="9" height="9" viewBox="0 0 9 9"><circle cx="3.7" cy="3.7" r="2.7" stroke="#999" stroke-width="1.3" fill="none"/><path d="M5.8 5.8L8.5 8.5" stroke="#999" stroke-width="1.4"/></svg>
    </nav>
  </header>

  <section>
    <div class="abs hero" role="img" aria-label="Featured fluid art painting in swirling green, purple and gold"></div>
    <div class="abs fade-top" role="img" aria-label="Soft paper edge"></div>
    <div class="abs fade-bottom" role="img" aria-label="Soft paper edge"></div>
    <div class="abs hero-dots"><i class="on"></i><i></i><i></i><i></i></div>
  </section>

  <section>
    <h2 class="abs section-badge">Creativity</h2>
    <p class="abs intro">Present your projects beautifully with unlimited styles – standard, overlayed or list view in grid, masonry or carousel fashion,<br>link projects to products in shop and even combine them divided by category. The choice is yours.</p>

    <article class="abs card" style="left:144px">
      <div class="art art-warm" role="img" aria-label="Fluid painting in amber, rust and cream"></div>
      <span class="caption">Drawing Name 1</span>
      <span class="zoom"><svg width="7" height="7" viewBox="0 0 9 9"><circle cx="3.7" cy="3.7" r="2.7" stroke="#333" stroke-width="1.4" fill="none"/><path d="M5.8 5.8L8.5 8.5" stroke="#333" stroke-width="1.5"/></svg></span>
    </article>
    <article class="abs card" style="left:331px">
      <div class="art art-night" role="img" aria-label="Fluid painting in deep blue with pale blossoms"></div>
      <span class="caption">Drawing Name 2</span>
      <span class="zoom"><svg width="7" height="7" viewBox="0 0 9 9"><circle cx="3.7" cy="3.7" r="2.7" stroke="#333" stroke-width="1.4" fill="none"/><path d="M5.8 5.8L8.5 8.5" stroke="#333" stroke-width="1.5"/></svg></span>
    </article>
    <article class="abs card" style="left:518px">
      <div class="art art-warm" role="img" aria-label="Fluid painting in amber, rust and cream"></div>
      <span class="caption">Drawing Name 3</span>
      <span class="zoom"><svg width="7" height="7" viewBox="0 0 9 9"><circle cx="3.7" cy="3.7" r="2.7" stroke="#333" stroke-width="1.4" fill="none"/><path d="M5.8 5.8L8.5 8.5" stroke="#333" stroke-width="1.5"/></svg></span>
    </article>

    <a class="abs shop-btn">SHOP NOW</a>
  </section>

  <section>
    <div class="abs rule" style="top:949px"></div>
    <p class="abs follow">Follow Me</p>
    <span class="abs social" style="left:399px" aria-label="Friendloop">F</span>
    <span class="abs social" style="left:423px" aria-label="Chirply">C</span>
    <span class="abs social" style="left:447px" aria-label="Snapvista">S</span>
    <span class="abs social" style="left:471px" aria-label="Pinspot">P</span>
    <span class="abs social" style="left:494px" aria-label="Vidreel">V</span>
    <div class="abs rule" style="top:997px"></div>
  </section>

  <footer>
    <div class="abs footer"></div>
    <div class="abs footer-fade" role="img" aria-label="Soft paper edge"></div>

    <h3 class="abs col-title" style="left:229px">Quick Links</h3>
    <span class="abs link" style="left:229px;top:1081px">Home</span>
    <span class="abs link" style="left:229px;top:1094px">About</span>
    <span class="abs link" style="left:229px;top:1107px">Shop</span>
    <span class="abs link" style="left:229px;top:1120px">Cart</span>
    <span class="abs link" style="left:229px;top:1133px">Contact</span>

    <h3 class="abs col-title" style="left:329px">Contact Info</h3>
    <svg class="abs" style="left:330px;top:1083px" width="6" height="6" viewBox="0 0 6 6"><path d="M1 0l1.3 1.6-.7.8c.4.8 1 1.4 1.8 1.8l.8-.7L6 4.8 5 6C2.5 5.8.2 3.5 0 1z" fill="#fff"/></svg>
    <span class="abs link" style="left:343px;top:1081px">+1 555 0142 7788</span>
    <svg class="abs" style="left:330px;top:1099px" width="6" height="5" viewBox="0 0 6 5"><rect width="6" height="5" fill="#fff"/><path d="M0 0l3 2.5L6 0" stroke="#2b5a60" stroke-width=".7" fill="none"/></svg>
    <span class="abs link" style="left:343px;top:1097px">breckellgallery@mailorbit.net</span>
    <svg class="abs" style="left:330px;top:1114px" width="6" height="6" viewBox="0 0 6 6"><circle cx="3" cy="3" r="2.7" fill="none" stroke="#fff" stroke-width=".7"/><path d="M0.3 3h5.4M3 .3c-1.4 1.6-1.4 3.8 0 5.4M3 .3c1.4 1.6 1.4 3.8 0 5.4" stroke="#fff" stroke-width=".5" fill="none"/></svg>
    <span class="abs link" style="left:345px;top:1113px">monabreckellgallery.com</span>

    <h3 class="abs col-title" style="left:504px">Payment Info</h3>
    <span class="abs pay" style="left:503px">Payva</span>
    <span class="abs pay" style="left:527px">Cardo</span>
    <span class="abs pay" style="left:551px">Monix</span>
    <span class="abs pay" style="left:575px">Amtrel</span>

    <div class="abs base">© 2020, All Rights Reserved , Mona Breckell</div>
  </footer>

</div>
</body>
</html>
```